Greek Yogurt Design

Design Brief – Premium Greek Yogurt Line (150g Pot)
Background
We are a small-to-medium dairy producer launching a new premium Greek yogurt range. This line will come in slightly larger pots than our standard yogurts, and we are targeting an upmarket clientele with a higher price point.
Product Details
Product: Greek Yogurt (fruit on the bottom, yogurt on top)
Flavours:
Natural
Strawberry
Forest Fruit
Peach & Apricot
Vanilla
Mango
Weight: 150g
Kosher Certification: 2 logos must be applied neatly (logos provided).
Lid: Standard universal lid (not flavour-specific).
Design Style
Clean, elegant, and premium feel (avoid clutter).
Should stand out as sophisticated compared to our standard range.
Visual hierarchy:
Brand & product type (Greek Yogurt) should be clear.
Flavour indicated with subtle but distinct cues (colour palette, fruit illustration/photography).
“Fruit on the bottom” message should be communicated simply.
Premium cues: minimalist typography, restrained colour palette, elegant fruit imagery.
References / Inspiration
Velmora Yogurt
– clean, bold, dairy-traditional.
Brask Dairy Greek Style
– natural, elegant design.
Lunaro Greek Yogurt
– modern, colourful yet clean.
Deliverables
Pot sleeve / pot design (to wrap around container).
Must work across all flavours with colour/flavour variation.
Space for universal lid (do not design individual lids).
Application of 2 kosher logos in a balanced way.
Updates
Industry/Entity Type
Dairy
Colors
Designer to choose colors to be used in the design.
Look and feel
Each slider illustrates characteristics of the customer's brand and the style your logo design should communicate.

```html
<!DOCTYPE html>
<html lang="en">
<head>
<meta charset="utf-8">
<title>Sorvela Greek Yogurt – Vanilla Pot Sleeve</title>
<link rel="stylesheet" href="https://fonts.googleapis.com/css2?family=Fraunces:opsz,wght@9..144,400&family=Outfit:wght@300;400;700&family=Pacifico&display=swap">
<style>
  :root {
    --stage: #d3d4d8;
    --sleeve: #f4f4f3;
    --ink: #222222;
    --muted: #4a4a4a;
    --brand-green: #5bb53b;
    --gold-light: #f3ecb4;
    --gold: #e2d36e;
    --gold-deep: #cdb94a;
    --vanilla-light: #e9cf9c;
    --vanilla-mid: #c9a56b;
    --vanilla-dark: #2f3327;
  }
  * { box-sizing: border-box; margin: 0; padding: 0; }
  html, body {
    width: 1200px; height: 900px; overflow: hidden;
    background: var(--stage);
  }
  .sleeve {
    position: absolute; left: 150px; top: 170px;
    width: 900px; height: 560px;
    background: var(--sleeve);
    overflow: hidden;
  }
  .rim-band {
    position: absolute; left: 0; top: 0; width: 100%; height: 58px;
    background: linear-gradient(90deg, var(--gold-deep), var(--gold) 30%, var(--gold-light) 50%, var(--gold) 70%, var(--gold-deep));
  }
  .nutrition {
    position: absolute; left: 40px; top: 105px; width: 118px;
    font-family: "Outfit", sans-serif; font-size: 8px; color: var(--muted);
    border: 1px solid var(--muted); padding: 5px 6px;
  }
  .nutrition h3 { font-size: 9px; font-weight: 700; border-bottom: 1px solid var(--muted); margin-bottom: 3px; padding-bottom: 2px; }
  .nutrition .row { display: flex; justify-content: space-between; line-height: 13px; }
  .storage-note {
    position: absolute; left: 40px; top: 348px; width: 118px;
    font-family: "Outfit", sans-serif; font-size: 8px; color: var(--muted);
  }
  .front {
    position: absolute; left: 250px; top: 100px; width: 400px;
    text-align: center;
  }
  .brand-name {
    display: inline-flex; align-items: center; gap: 8px;
    font-family: "Outfit", sans-serif; font-weight: 700; font-size: 34px;
    color: var(--brand-green);
  }
  .brand-dot { width: 14px; height: 14px; border-radius: 50%; background: var(--brand-green); }
  .product-type {
    font-family: "Fraunces", serif; font-weight: 400; color: var(--ink);
    font-size: 94px; line-height: 0.98; letter-spacing: -1px;
    margin-top: 8px;
  }
  .flavour-tag {
    display: inline-block; margin-top: 40px;
    background: var(--gold); color: #fff;
    font-family: "Pacifico", cursive; font-size: 15px;
    padding: 1px 26px 4px;
  }
  .claim {
    margin-top: 8px;
    font-family: "Outfit", sans-serif; font-weight: 300; font-size: 16px; color: var(--muted);
  }
  .flavour-visual {
    position: absolute; right: 40px; top: 80px; width: 190px; height: 480px;
    background: linear-gradient(170deg, var(--vanilla-light) 0%, var(--vanilla-mid) 55%, var(--vanilla-dark) 100%);
    border-radius: 90px 90px 0 0;
    opacity: 0.85;
  }
</style>
</head>
<body>
  <div class="sleeve">
    <div class="rim-band"></div>

    <div class="nutrition">
      <h3>Nutrition Facts</h3>
      <div class="row"><span>Daily Value*</span><span></span></div>
      <div class="row"><span>Energy</span><span>96.7 Kcal</span></div>
      <div class="row"><span>Fat</span><span>3.8 g</span></div>
      <div class="row"><span>Protein</span><span>14.9 g</span></div>
      <div class="row"><span>Carbs</span><span>13.8 g</span></div>
      <div class="row"><span>Sugars</span><span>1.5 g</span></div>
      <div class="row"><span>Sat. fat</span><span>0.9 g</span></div>
      <div class="row"><span>Fibre</span><span>0 g</span></div>
      <div class="row"><span>Calcium</span><span>8 mg</span></div>
      <div class="row"><span>Sodium</span><span>1 mg</span></div>
    </div>
    <p class="storage-note">Store chilled below 5°C</p>

    <div class="front">
      <div class="brand-name"><span class="brand-dot"></span>Sorvela</div>
      <h1 class="product-type">Greek<br>Yogurt</h1>
      <div class="flavour-tag">Vanilla</div>
      <p class="claim">Fruit on the bottom, yogurt on top</p>
    </div>

    <div class="flavour-visual" role="img" aria-label="Photograph of vanilla flowers and vanilla pods"></div>
  </div>
</body>
</html>
```